Marlow Realty Real Estate Brokerage Recruiting Flyer

We are a real estate brokerage looking to hire more real estate agents. We need to list everything we have to offer as a company so real estate agents will join our company. this is our company website: www.Marlowrealty.example .

100% COMMISSION NO MONTHLY FEE
$450 Flat Transaction FEE

What We Offer:
24/7 Office Access
Free E & O Insurance for 1st Year
Free Online CE and PLE
Free 1,000 Business Cards
Free Professional Social Media Marketing
Free Printing, Scanning, and Copies
Free Buyer and Seller Presentation Packages
Free Filquay Cloud Based Document Management Access
Access to our Internal Brokerage Forum
Company Profit Sharing!
Private Offices Available to Rent

*Lead Generation Software with over 3,000 Leads
*10 Leads to Start
* Free Personal CRM and Website
*Restrictions and Rules apply

Company Address:
4817 Amberfield Road
Suite 512
Fairfax, VA 22194
Phone: 703-555-0147
email: info@marlowrealty.example

Target Market(s)

Real Estate Agents

Industry/Entity Type

Real Estate

Colors
0555a3
ffffff

Requirements
Must have
• 100% COMMISSION NO MONTHLY FEE
$450 Flat Transaction FEE

What We Offer:
24/7 Office Access
Free Online CE and PLE
Free 1,000 Business Cards
Company Profit Sharing!

*10 Leads to Start

Company Address:
4817 Amberfield Road
Suite 512
Fairfax, VA 22194
Phone: 703-555-0147

```html
<!DOCTYPE html>
<html lang="en">
<head>
<meta charset="utf-8">
<title>Marlow Realty – We Are Hiring</title>
<link rel="stylesheet" href="https://fonts.googleapis.com/css2?family=Poppins:ital,wght@0,700;0,800;1,700&family=Didact+Gothic&display=swap">
<style>
  :root {
    --brand-blue: #0555a3;
    --accent-orange: #fbad18;
    --white: #ffffff;
    --photo-light: #e9e4dc;
    --photo-mid: #c9c2b8;
    --photo-dark: #8d8a88;
  }
  html, body { margin: 0; padding: 0; overflow: hidden; background: var(--white); }
  .flyer { display: block; width: 927px; height: 1200px; }
  .headline { font-family: "Poppins", sans-serif; font-weight: 800; }
  .headline--white { fill: var(--white); }
  .headline--orange { fill: var(--accent-orange); }
  .brand-name { font-family: "Didact Gothic", sans-serif; font-size: 28px; fill: var(--brand-blue); }
  .offer-title { font-family: "Poppins", sans-serif; font-weight: 700; font-size: 53px; fill: var(--white); }
  .offer-item { font-family: "Didact Gothic", sans-serif; font-size: 23px; fill: var(--white); }
  .perk { font-family: "Poppins", sans-serif; font-weight: 700; font-style: italic; font-size: 21.5px; fill: var(--white); }
  .tick-circle { fill: var(--accent-orange); }
  .tick-mark { fill: none; stroke: var(--white); stroke-width: 2.4; stroke-linecap: round; stroke-linejoin: round; }
  .deal { font-family: "Poppins", sans-serif; font-weight: 800; fill: var(--white); }
  .deal-fee { font-family: "Poppins", sans-serif; font-weight: 700; font-size: 27px; fill: var(--white); }
  .contact-title { font-family: "Poppins", sans-serif; font-weight: 800; font-size: 38px; fill: var(--brand-blue); }
  .contact-text { font-family: "Didact Gothic", sans-serif; font-size: 23.5px; fill: var(--brand-blue); }
  .contact-phone { font-family: "Didact Gothic", sans-serif; font-size: 22px; fill: var(--brand-blue); }
  .contact-link { font-family: "Didact Gothic", sans-serif; font-size: 16px; fill: var(--brand-blue); }
  .icon-circle { fill: var(--brand-blue); }
  .icon-line { fill: none; stroke: var(--white); stroke-width: 1.6; stroke-linecap: round; stroke-linejoin: round; }
  .license { font-family: "Didact Gothic", sans-serif; font-style: italic; font-size: 16.5px; fill: var(--brand-blue); }
</style>
</head>
<body>
<svg class="flyer" viewBox="0 0 927 1200" xmlns="http://www.w3.org/2000/svg">
  <defs>
    <linearGradient id="photoTone" x1="0" y1="0" x2="1" y2="1">
      <stop offset="0" stop-color="var(--photo-mid)"/>
      <stop offset="0.45" stop-color="var(--photo-light)"/>
      <stop offset="1" stop-color="var(--photo-dark)"/>
    </linearGradient>
  </defs>

  <rect width="927" height="1200" fill="var(--white)"/>

  <path role="img" aria-label="Photo of two people in suits shaking hands behind a small wooden model house and a set of house keys on a desk"
        d="M0,0 H927 V410 C800,505 660,568 470,572 C300,574 150,505 0,398 Z" fill="url(#photoTone)"/>

  <path class="panel-offer" d="M0,418 C150,520 300,585 460,593 L460,1200 L0,1200 Z" fill="var(--brand-blue)"/>
  <path class="panel-deal" d="M478,593 C660,590 810,525 927,425 L927,896 L478,896 Z" fill="var(--accent-orange)"/>

  <g class="brand">
    <rect x="672" y="36" width="24" height="24" fill="var(--brand-blue)"/>
    <text class="brand-name" x="912" y="58" text-anchor="end" textLength="200" lengthAdjust="spacingAndGlyphs">Marlow Realty</text>
  </g>

  <text class="headline headline--white" x="38" y="280" font-size="118" textLength="470" lengthAdjust="spacingAndGlyphs">WE ARE</text>
  <text class="headline headline--orange" x="40" y="395" font-size="118" textLength="466" lengthAdjust="spacingAndGlyphs">HIRING!</text>

  <text class="offer-title" x="17" y="582">WHAT</text>
  <text class="offer-title" x="17" y="632" textLength="265" lengthAdjust="spacingAndGlyphs">WE OFFER:</text>

  <g class="offer-ticks">
    <g transform="translate(30,665)"><circle class="tick-circle" r="10.5"/><path class="tick-mark" d="M-5,0 L-1.5,4 L5,-3.5"/></g>
    <g transform="translate(30,692)"><circle class="tick-circle" r="10.5"/><path class="tick-mark" d="M-5,0 L-1.5,4 L5,-3.5"/></g>
    <g transform="translate(30,719)"><circle class="tick-circle" r="10.5"/><path class="tick-mark" d="M-5,0 L-1.5,4 L5,-3.5"/></g>
    <g transform="translate(30,747)"><circle class="tick-circle" r="10.5"/><path class="tick-mark" d="M-5,0 L-1.5,4 L5,-3.5"/></g>
    <g transform="translate(30,774)"><circle class="tick-circle" r="10.5"/><path class="tick-mark" d="M-5,0 L-1.5,4 L5,-3.5"/></g>
    <g transform="translate(30,829)"><circle class="tick-circle" r="10.5"/><path class="tick-mark" d="M-5,0 L-1.5,4 L5,-3.5"/></g>
    <g transform="translate(30,856)"><circle class="tick-circle" r="10.5"/><path class="tick-mark" d="M-5,0 L-1.5,4 L5,-3.5"/></g>
    <g transform="translate(30,911)"><circle class="tick-circle" r="10.5"/><path class="tick-mark" d="M-5,0 L-1.5,4 L5,-3.5"/></g>
    <g transform="translate(30,965)"><circle class="tick-circle" r="10.5"/><path class="tick-mark" d="M-5,0 L-1.5,4 L5,-3.5"/></g>
    <g transform="translate(30,993)"><circle class="tick-circle" r="10.5"/><path class="tick-mark" d="M-5,0 L-1.5,4 L5,-3.5"/></g>
    <g transform="translate(30,1020)"><circle class="tick-circle" r="10.5"/><path class="tick-mark" d="M-5,0 L-1.5,4 L5,-3.5"/></g>
  </g>

  <g class="offer-list">
    <text class="offer-item" x="51" y="673">24/7 Office Access</text>
    <text class="offer-item" x="51" y="700">Free E &amp; O Insurance for 1st Year</text>
    <text class="offer-item" x="51" y="727">Free Online CE and PLE</text>
    <text class="offer-item" x="51" y="755">Free 1,000 Business Cards</text>
    <text class="offer-item" x="51" y="782">Free Professional Social Media</text>
    <text class="offer-item" x="51" y="809">Marketing</text>
    <text class="offer-item" x="51" y="837">Free Printing, Scanning, and Copies</text>
    <text class="offer-item" x="51" y="864">Free Buyer and Seller Presentation</text>
    <text class="offer-item" x="51" y="891">Packages</text>
    <text class="offer-item" x="51" y="919">Free Filquay Cloud Based Document</text>
    <text class="offer-item" x="51" y="946">Management Access</text>
    <text class="offer-item" x="51" y="973" textLength="400" lengthAdjust="spacingAndGlyphs">Access to our Internal Brokerage Forum</text>
    <text class="offer-item" x="51" y="1001">Company Profit Sharing!</text>
    <text class="offer-item" x="51" y="1028">Private Offices Available to Rent</text>
  </g>

  <g class="perks">
    <text class="perk" x="22" y="1071">*</text><text class="perk" x="48" y="1071" textLength="400" lengthAdjust="spacingAndGlyphs">Lead Generation Software with over</text>
    <text class="perk" x="48" y="1098">3,000 Leads</text>
    <text class="perk" x="22" y="1125">*</text><text class="perk" x="48" y="1125">10 Leads to Start</text>
    <text class="perk" x="22" y="1153">*</text><text class="perk" x="48" y="1153">Free Personal CRM and Website</text>
    <text class="perk" x="22" y="1180">*</text><text class="perk" x="48" y="1180">Restrictions and Rules apply</text>
  </g>

  <text class="deal" x="895" y="596" font-size="64" text-anchor="end">100%</text>
  <text class="deal" x="521" y="648" font-size="60" textLength="358" lengthAdjust="spacingAndGlyphs">COMMISSION</text>
  <rect x="526" y="657" width="356" height="4" fill="var(--white)"/>
  <text class="deal" x="527" y="714" font-size="60" textLength="355" lengthAdjust="spacingAndGlyphs">NO MONTHLY</text>
  <text class="deal" x="526" y="843" font-size="172" textLength="360" lengthAdjust="spacingAndGlyphs">FEES</text>
  <text class="deal-fee" x="528" y="878" textLength="352" lengthAdjust="spacingAndGlyphs">$450 Flat Transaction FEE</text>

  <text class="contact-title" x="484" y="947" textLength="412" lengthAdjust="spacingAndGlyphs">CONTACT US FOR MORE</text>
  <text class="contact-title" x="484" y="980">INFORMATION:</text>

  <text class="contact-text" x="484" y="1028">MARLOW REALTY</text>
  <text class="contact-text" x="484" y="1063">4817 Amberfield</text>
  <text class="contact-text" x="484" y="1097">Road Suite 512</text>
  <text class="contact-text" x="484" y="1132">Fairfax, VA 22194</text>

  <g class="icon icon--phone" transform="translate(718,1019)">
    <circle class="icon-circle" r="16"/>
    <path class="icon-line" d="M-6,-7 L-3,-8 L-1,-3 L-3,-1.5 C-2,1.5 0,3.5 2,4.5 L3.5,2.5 L8,4.5 L7,7.5 C0,8 -7,1 -6,-7 Z"/>
  </g>
  <text class="contact-phone" x="744" y="1027">703-555-0147</text>

  <g class="icon icon--mail" transform="translate(718,1068)">
    <circle class="icon-circle" r="16"/>
    <rect class="icon-line" x="-8" y="-6" width="16" height="12" rx="1"/>
    <path class="icon-line" d="M-8,-5 L0,1 L8,-5"/>
  </g>
  <text class="contact-link" x="742" y="1074" textLength="170" lengthAdjust="spacingAndGlyphs">info@marlowrealty.example</text>

  <g class="icon icon--web" transform="translate(718,1117)">
    <circle class="icon-circle" r="16"/>
    <circle class="icon-line" r="8.5"/>
    <ellipse class="icon-line" rx="3.8" ry="8.5"/>
    <path class="icon-line" d="M-8.5,0 H8.5 M-7,-4.5 H7 M-7,4.5 H7"/>
  </g>
  <text class="contact-link" x="742" y="1123" textLength="170" lengthAdjust="spacingAndGlyphs">www.Marlowrealty.example</text>

  <text class="license" x="914" y="1178" text-anchor="end">Licensed in D.C., Maryland, and Virginia</text>
</svg>
</body>
</html>
```